Banner ad to sell prefabricated holiday homes in New Zealand

Harbourlight Homes build prefabricated homes in a factory that are then transported by truck to their site. It's coming into summer here in New Zealand and many people will be thinking about the holidays and wishing they had a holiday home.

The design should communicate some of the following benefits of our homes:
- Full project management
- Great value for money
- Delivered complete with all interior & exterior fittings
- Quality construction in our controlled factory

The banner ad will be displayed on a popular weather website www.skyreport.co.nz
Size: 760px x 120px
Would like it to be animated if but the size must be below 60kb.

I'll upload some nice holiday destination photos for backgrounds & some pictures of our holiday home designs for you to use.
Our main company colors are bright blue (pantone 3005) and light grey/silver.

Updatefor brief:
I would like the animation to show different text so that it's not all squashed up on the one image.
For example have "Prefabricated Holiday Homes" on one image & then it fades/changes to next image with "Delivered complete with all interior & exterior fittings". Or something like that with nice background images or pictures of our houses.

Font styles to use
Sans Serif

Colors
3176b5
0d5aa6
33a6d7
3276b5

Requirements
Nice to have
• Our logo

```html
<!DOCTYPE html>
<html lang="en">
<head>
<meta charset="utf-8">
<title>Harbourlight Homes – Holiday Homes Banner</title>
<link rel="stylesheet" href="https://fonts.googleapis.com/css2?family=Roboto:wght@500;700&family=Roboto+Condensed:wght@700&display=swap">
<style>
  :root {
    --page-bg: #ececec;
    --blue-deep: #0d5aa6;
    --blue-mid: #3176b5;
    --blue-bright: #33a6d7;
    --ink: #1c2b3a;
    --white: #ffffff;
    --note-grey: #9c9c9c;
    --cta-top: #ffd83a;
    --cta-bottom: #f3a800;
    --cta-ink: #1a2a40;
  }
  * { margin: 0; padding: 0; box-sizing: border-box; }
  html, body {
    width: 1200px; height: 272px; overflow: hidden;
    background: var(--page-bg);
    font-family: "Roboto", Arial, sans-serif;
  }
  .stage { position: relative; width: 1200px; height: 272px; }

  .banner {
    position: absolute; left: 102px; top: 26px;
    width: 1080px; height: 160px; overflow: hidden;
  }
  .banner-shapes { position: absolute; inset: 0; }

  .benefits {
    position: absolute; left: 14px; top: 10px;
    list-style: none; color: var(--white);
    font-weight: 700; font-size: 16.5px; line-height: 19px;
  }
  .benefits li { position: relative; padding-left: 12px; margin-bottom: 3px; }
  .benefits li::before {
    content: ""; position: absolute; left: 0; top: 7px;
    width: 5px; height: 5px; border-radius: 50%; background: var(--white);
  }

  .brand {
    position: absolute; left: 716px; top: 38px;
    display: flex; align-items: center; gap: 12px;
  }
  .brand-mark {
    width: 46px; height: 46px; background: var(--blue-mid);
  }
  .brand-name {
    font-weight: 500; font-size: 23px; color: var(--ink); white-space: nowrap;
  }

  .cta {
    position: absolute; left: 756px; top: 94px;
    width: 196px; height: 40px; border-radius: 20px;
    background: linear-gradient(var(--cta-top), var(--cta-bottom));
    border: 1px solid #d08f00;
    box-shadow: 0 2px 3px rgba(0,0,0,.3);
    display: flex; align-items: center; justify-content: center; gap: 10px;
    font-weight: 700; font-size: 18px; color: var(--cta-ink);
    text-decoration: none;
  }
  .cta svg { display: block; }

  .animation-note {
    position: absolute; left: 0; right: 0; top: 224px;
    text-align: center;
    font-family: "Roboto Condensed", "Arial Narrow", sans-serif;
    font-weight: 700; font-size: 33px; letter-spacing: .2px;
    color: var(--note-grey); text-transform: uppercase;
  }
</style>
</head>
<body>
<div class="stage">
  <div class="banner">
    <svg class="banner-shapes" width="1080" height="160" viewBox="0 0 1080 160">
      <defs>
        <linearGradient id="panelBlue" x1="0" y1="0" x2="0" y2="1">
          <stop offset="0" stop-color="var(--blue-bright)"/>
          <stop offset=".55" stop-color="var(--blue-mid)"/>
          <stop offset="1" stop-color="var(--blue-deep)"/>
        </linearGradient>
        <linearGradient id="photoTones" x1="0" y1="0" x2="0" y2="1">
          <stop offset="0" stop-color="#c7d3dc"/>
          <stop offset=".35" stop-color="#aab7bf"/>
          <stop offset=".55" stop-color="#3f4f6a"/>
          <stop offset=".78" stop-color="#8a8a73"/>
          <stop offset="1" stop-color="#b8b1a2"/>
        </linearGradient>
      </defs>
      <rect x="250" y="0" width="480" height="160" fill="url(#photoTones)" role="img" aria-label="Photo of a navy blue prefabricated holiday home with a timber deck on a landscaped section"/>
      <path d="M0 0 H286 Q300 80 272 160 H0 Z" fill="url(#panelBlue)"/>
      <path d="M286 0 Q300 80 272 160" fill="none" stroke="#ffffff" stroke-width="3" opacity=".85"/>
      <path d="M716 0 H1080 V160 H696 Q672 80 716 0 Z" fill="url(#panelBlue)"/>
      <path d="M716 0 Q672 80 696 160" fill="none" stroke="#ffffff" stroke-width="3" opacity=".85"/>
      <path d="M700 92 Q760 20 1080 22 V78 Q860 64 700 92 Z" fill="#ffffff" opacity=".96"/>
    </svg>

    <ul class="benefits">
      <li>Full project management</li>
      <li>Great value for money</li>
      <li>Delivered complete with<br>all interior &amp; exterior fittings</li>
      <li>Quality construction in<br>our controlled factory</li>
    </ul>

    <div class="brand">
      <span class="brand-mark"></span>
      <span class="brand-name">Harbourlight Homes</span>
    </div>

    <a class="cta" href="#">Find Out More
      <svg width="10" height="14" viewBox="0 0 10 14"><path d="M2 1 L8 7 L2 13" fill="none" stroke="#1a2a40" stroke-width="2.5"/></svg>
    </a>
  </div>

  <p class="animation-note">See the link in the description to view the animation</p>
</div>
</body>
</html>
```